Investment company needing business card

We are wanting a business card which looks sharp and easy on the eye. We are thinking of having a business card with the logo embossed on it, to really make it stand out. We will only have a small amount of information of the business card, person's name, position, email address and phone number

Contact Information for Business Card

Danica Pruett
Executive Assistant
+64 21 547 3162
danicap@harwellcapital.co.nz

Requirements
Must have
• Embossed logo
Should not have
• Not to be busy

```html
<!DOCTYPE html>
<html lang="en">
<head>
<meta charset="utf-8">
<title>Harwell Capital – Business Card</title>
<link rel="stylesheet" href="https://fonts.googleapis.com/css2?family=Titillium+Web:wght@400;600&display=swap">
<style>
  :root {
    --backdrop: #ece7df;
    --card: #ffffff;
    --brand-green: #23b573;
    --brand-grey: #616161;
    --ink: #4a4a4a;
    --rule: #5c5c5c;
  }
  * { box-sizing: border-box; margin: 0; padding: 0; }
  html, body {
    width: 1200px;
    height: 1200px;
    overflow: hidden;
  }
  body {
    background: var(--backdrop);
    font-family: "Titillium Web", sans-serif;
    position: relative;
  }
  .card {
    position: absolute;
    left: 333px;
    width: 534px;
    height: 346px;
    background: var(--card);
    box-shadow: 0 3px 8px rgba(0, 0, 0, 0.18);
    overflow: hidden;
  }
  .card--front { top: 209px; }
  .card--back { top: 631px; }

  .brand-panel {
    position: absolute;
    left: 0;
    top: 0;
    width: 259px;
    height: 100%;
    background: linear-gradient(160deg, var(--brand-green) 0%, var(--brand-green) 45%, var(--brand-grey) 100%);
  }

  .brand-name {
    position: absolute;
    color: var(--brand-green);
    font-weight: 600;
    text-transform: uppercase;
    letter-spacing: 0.5px;
    white-space: nowrap;
    line-height: 1;
  }
  .card--front .brand-name {
    left: 259px;
    width: 275px;
    top: 34px;
    text-align: center;
    font-size: 20px;
  }

  .brand-lockup {
    position: absolute;
    left: 0;
    right: 0;
    top: 40px;
    display: flex;
    justify-content: center;
    align-items: center;
    gap: 14px;
  }
  .brand-lockup .brand-square {
    width: 56px;
    height: 56px;
    background: var(--brand-grey);
  }
  .brand-lockup .brand-name {
    position: static;
    font-size: 34px;
  }

  .holder-name {
    position: absolute;
    left: 28px;
    top: 168px;
    font-size: 25px;
    font-weight: 400;
    color: var(--brand-green);
    line-height: 1;
  }
  .holder-role {
    position: absolute;
    left: 28px;
    top: 200px;
    display: flex;
    align-items: center;
    width: 475px;
    font-size: 13px;
    color: var(--ink);
    line-height: 1;
  }
  .holder-role::after {
    content: "";
    flex: 1;
    height: 3px;
    margin-left: 6px;
    background: var(--rule);
  }

  .contact-list {
    position: absolute;
    left: 30px;
    top: 264px;
    list-style: none;
    font-size: 13.5px;
    color: var(--ink);
    line-height: 18px;
  }
  .contact-list li {
    display: flex;
    align-items: center;
    gap: 12px;
  }
  .contact-icon {
    width: 11px;
    height: 11px;
    flex: none;
  }
</style>
</head>
<body>
  <section class="card card--front" aria-label="Business card front">
    <div class="brand-panel" role="img" aria-label="Brand mark area in green and grey"></div>
    <div class="brand-name">Harwell Capital</div>
  </section>

  <section class="card card--back" aria-label="Business card back">
    <div class="brand-lockup">
      <span class="brand-square" aria-hidden="true"></span>
      <span class="brand-name">Harwell Capital</span>
    </div>

    <h1 class="holder-name">Danica Pruett</h1>
    <p class="holder-role">Executive Assistant</p>

    <ul class="contact-list">
      <li>
        <svg class="contact-icon" viewBox="0 0 12 12" aria-hidden="true">
          <circle cx="6" cy="6" r="6" fill="var(--brand-green)"/>
          <path d="M4 3.2c.4-.3.7-.2.9.2l.4.8c.1.3 0 .5-.2.7l-.3.2c.3.7.8 1.2 1.5 1.5l.2-.3c.2-.2.4-.3.7-.2l.8.4c.4.2.5.5.2.9-.5.7-1.3.8-2.3.2C5 7 4.6 6.5 4.1 5.7 3.5 4.6 3.5 3.7 4 3.2z" fill="#fff"/>
        </svg>
        <span>+64 21 547 3162</span>
      </li>
      <li>
        <svg class="contact-icon" viewBox="0 0 12 12" aria-hidden="true">
          <circle cx="6" cy="6" r="6" fill="var(--brand-green)"/>
          <rect x="3" y="4" width="6" height="4" fill="#fff"/>
          <path d="M3 4l3 2.2L9 4" fill="none" stroke="var(--brand-green)" stroke-width="0.8"/>
        </svg>
        <span>danicap@harwellcapital.co.nz</span>
      </li>
    </ul>
  </section>
</body>
</html>
```